Verin Court Nine Flash website

we need a website to cater to 2 aspect of the business. We have Verin court residence and verin court office. For the office, we will get their inquire and arrange a face to face meetup to show them the office area for rent. For the residence side, it will need to be like lodgly or staymira.com. we want to allow them to book online for the date they need. We have a total of 10 different room configurations starting at $70 per night and up depending on the size of the room. example of the design is https://pelvandale.com/

Target Market(s)

the website should have detail information on the layout, designs, and luxury of the building.

Industry/Entity Type

office and service appartment rental/lease

Coding

Coded - Design and coding required

Number of Pages Required

5+ page

Requirements
Must have
• a luxury perspective
Nice to have
• example https://pelvandale.com/

```html
<!DOCTYPE html>
<html lang="en">
<head>
<meta charset="utf-8">
<title>Verin Court Nine — Find Your Dream Property</title>
<link href="https://fonts.googleapis.com/css2?family=Gilda+Display&family=Marcellus&family=Poppins:wght@300;400;500;600&display=swap" rel="stylesheet">
<style>
:root{
  --gold:#c9a24a;
  --gold-light:#f3e27a;
  --gold-deep:#a87a2c;
  --brown:#3a2a18;
  --dark:#1b1713;
  --ink:#2a2520;
  --muted:#7b746c;
  --cream:#fbf7f1;
  --cream-2:#f7f1e6;
  --white:#ffffff;
  --line:#e9e1d3;
}
*{box-sizing:border-box;margin:0;padding:0}
html,body{width:1200px;height:3966px;overflow:hidden}
body{position:relative;background:var(--white);font-family:"Poppins",sans-serif;color:var(--ink)}
.abs{position:absolute}
.serif{font-family:"Gilda Display",serif}
ul{list-style:none}

/* Header */
.hero{position:absolute;left:0;top:0;width:1200px;height:578px;background:linear-gradient(180deg,#5d5e60 0%,#6d6a66 30%,#4a3f34 62%,#5a3a22 85%,#3a2616 100%)}
.nav{position:absolute;left:0;top:0;width:1200px;height:86px}
.brand{position:absolute;left:130px;top:24px;display:flex;align-items:center;gap:12px;color:#f4eee4;font-family:"Marcellus",serif;font-size:23px;letter-spacing:.5px}
.brand .mark{width:34px;height:38px;background:var(--gold);display:block}
.menu{position:absolute;left:464px;top:38px;display:flex;gap:0;font-size:8.5px;font-weight:500;color:#fff;letter-spacing:.3px}
.menu li{position:absolute;white-space:nowrap}
.menu .active{color:var(--gold-light)}
.menu .active::after{content:"";position:absolute;left:0;right:0;top:14px;height:1.5px;background:var(--gold-light)}
.phone-btn{position:absolute;left:915px;top:29px;width:123px;height:28px;border-radius:14px;background:linear-gradient(90deg,#f4e27c,#d9b85a);display:flex;align-items:center;justify-content:center;gap:6px;font-size:8.5px;font-weight:500;color:var(--brown)}
.search-ic{position:absolute;left:1054px;top:36px}
.eyebrow{font-size:8px;letter-spacing:2.2px;font-weight:500;color:var(--gold);text-transform:uppercase;display:flex;align-items:center;justify-content:center;gap:12px}
.eyebrow::before,.eyebrow::after{content:"";width:34px;height:1px;background:currentColor;opacity:.6}
.hero-copy{position:absolute;left:0;top:164px;width:1200px;text-align:center;color:#fff}
.hero-copy h1{font-family:"Gilda Display",serif;font-weight:400;font-size:48px;line-height:57px;margin-top:18px}
.hero-copy p{font-size:12px;margin-top:10px}
.chev{position:absolute;left:591px;top:482px}
.quick-contact{position:absolute;left:1168px;top:226px;width:32px}
.quick-contact span{display:flex;width:32px;height:31px;align-items:center;justify-content:center}

/* Search */
.search{position:absolute;left:149px;top:520px;width:901px;height:58px;background:var(--white);border-radius:10px 10px 0 0;display:flex;align-items:center;padding:0 20px;gap:10px}
.field{width:135px;height:28px;border-radius:4px;background:#f1efec;display:flex;align-items:center;justify-content:space-between;padding:0 10px;font-size:8px;color:#6a635c}
.field b{font-weight:400;display:flex;align-items:center;gap:6px}
.search-btn{width:140px;height:28px;border-radius:4px;background:linear-gradient(90deg,#e8c75f,#c99b3a);font-size:8px;font-weight:600;color:var(--brown);display:flex;align-items:center;justify-content:center;gap:6px}

/* Reserve band + developers */
.dev-band{position:absolute;left:0;top:578px;width:1200px;height:283px;background:linear-gradient(90deg,#5d4422 0%,#866433 40%,#b68a47 75%,#c89a52 100%)}
.reserve{position:absolute;left:149px;top:0;width:901px;height:77px;border-radius:0 0 10px 10px;background:linear-gradient(90deg,#c59a4a 0%,#e6c869 45%,#f8ec84 100%);display:flex;align-items:center;padding:0 30px}
.reserve .brand-sm{display:flex;align-items:center;gap:10px;font-family:"Marcellus",serif;font-size:18px;color:#fff}
.reserve .brand-sm i{width:26px;height:30px;background:#f6e8c4;display:block}
.reserve h2{font-family:"Gilda Display",serif;font-weight:400;font-size:28px;color:var(--dark);margin-left:auto;margin-right:8px}
.dev-title{position:absolute;left:0;top:116px;width:1200px;color:#e2bf6d}
.dev-row{position:absolute;left:0;top:161px;width:1200px;height:69px}
.dev-row .logo{position:absolute;top:0;height:69px;display:flex;align-items:center;justify-content:center;font-family:"Marcellus",serif;font-size:13px;color:#fff;letter-spacing:1px;width:145px;text-align:center}
.dev-row .logo.on{background:#fff;color:#b02a22;border-radius:8px;font-weight:600}
.arrow{position:absolute;color:#fff;font-size:18px}
.emblem{position:absolute;width:60px;height:60px;border-radius:50%;background:#fff;display:flex;align-items:center;justify-content:center;box-shadow:0 2px 8px rgba(0,0,0,.08)}
.emblem i{width:18px;height:22px;background:var(--gold);display:block;opacity:.8}

/* Section headings */
.sec-head{position:absolute;left:0;width:1200px;text-align:center}
.sec-head h2{font-family:"Gilda Display",serif;font-weight:400;font-size:40px;margin-top:12px;color:var(--ink)}
.sec-head h2 em{font-style:normal;color:#a8844f}

/* Property card */
.card{position:absolute;width:205px;height:302px;background:#fff;border-radius:6px;box-shadow:0 4px 14px rgba(60,40,10,.1);overflow:hidden}
.card.featured{outline:2px solid #e9cf8f;box-shadow:0 6px 22px rgba(201,162,74,.45)}
.card-media{height:174px}
.card .star{position:absolute;left:12px;top:12px;width:17px;height:17px;border-radius:50%;background:var(--gold);display:flex;align-items:center;justify-content:center}
.card .gal{position:absolute;right:16px;top:164px;width:22px;height:22px;border-radius:50%;background:#fff;box-shadow:0 1px 4px rgba(0,0,0,.2);display:flex;align-items:center;justify-content:center}
.card.featured .gal{background:var(--gold-light);width:30px;height:30px;top:158px}
.card h3{font-family:"Gilda Display",serif;font-weight:400;font-size:16px;margin:18px 0 0 17px;color:var(--ink)}
.card p{font-size:8px;line-height:13px;color:var(--muted);margin:4px 14px 0 17px}
.specs{display:flex;gap:14px;margin:16px 0 0 17px;font-size:6.5px;color:var(--muted)}
.specs li{display:flex;align-items:center;gap:4px}

/* Launch */
.launch{position:absolute;left:0;top:1403px;width:1200px;height:584px;background:var(--cream)}
.tile{position:absolute;border-radius:4px;overflow:hidden}
.tile .tag{position:absolute;left:0;bottom:0;background:#fff;padding:6px 12px 2px 9px;font-family:"Gilda Display",serif;font-size:14px;color:var(--ink);border-radius:0 6px 0 0}
.tile .overlay{position:absolute;left:24px;bottom:28px;color:#fff;width:230px}
.tile .overlay h4{font-family:"Gilda Display",serif;font-weight:400;font-size:16px}
.tile .overlay p{font-size:8px;line-height:13px;margin-top:6px;opacity:.9}
.tile .go{position:absolute;right:18px;bottom:18px;width:26px;height:26px;border-radius:50%;background:#fff;display:flex;align-items:center;justify-content:center;font-size:12px;color:var(--ink)}

/* Partners */
.partners-title{position:absolute;left:0;top:2022px;width:1200px;display:flex;align-items:center;gap:22px;font-family:"Gilda Display",serif;font-size:12px;letter-spacing:2px;color:var(--ink)}
.partners-title::before,.partners-title::after{content:"";flex:1;height:1px;background:var(--line)}
.partner{position:absolute;top:2102px;width:130px;height:70px;display:flex;align-items:center;justify-content:center;font-family:"Marcellus",serif;font-size:15px;color:#333;letter-spacing:.5px}
.partner.on{background:#fff;border-radius:8px;box-shadow:0 4px 16px rgba(0,0,0,.12)}
.partner.on span{width:44px;height:44px;background:linear-gradient(180deg,#2e5aa0,#c9a24a)}

/* Featured */
.feat{position:absolute;left:0;top:2241px;width:1200px;height:536px;background:linear-gradient(180deg,#3a2a1c 0%,#201a14 45%,#120f0c 100%)}
.feat .sec-head h2{color:#fff}
.feat .sec-head h2 em{color:#e3c878}

/* Articles */
.post{position:absolute;height:190px;border-radius:6px;overflow:hidden;background:var(--cream-2);display:flex}
.post .ph{width:236px;height:190px;flex:none}
.post .txt{padding:26px 24px 0 25px;width:236px}
.post .date{font-size:7.5px;color:var(--gold);display:flex;align-items:center;gap:8px}
.post .date::after{content:"";width:26px;height:1px;background:currentColor}
.post h4{font-family:"Gilda Display",serif;font-weight:400;font-size:14.5px;line-height:18px;margin-top:7px;color:var(--ink)}
.post p{font-size:7.5px;line-height:12px;color:var(--muted);margin-top:6px}
.post .more{font-size:7.5px;color:var(--gold);margin-top:40px;display:flex;align-items:center;gap:8px}
.post .more::before{content:"";width:18px;height:1px;background:currentColor}
.post.dark{background:linear-gradient(90deg,#4a3618,#2a2016)}
.post.dark h4,.post.dark p{color:#fff}

.strip-title{position:absolute;left:0;top:3400px;width:1200px;text-align:center;font-family:"Gilda Display",serif;font-size:12px;letter-spacing:2px;color:var(--ink)}
.strip{position:absolute;left:0;top:3471px;width:1200px;height:153px;display:flex}
.strip div{width:150px;height:153px}

/* Footer */
.footer{position:absolute;left:0;top:3624px;width:1200px;height:342px;background:linear-gradient(180deg,#1a1714,#121110);border-top:2px solid var(--gold-deep);color:#cfc8bd}
.f-brand{position:absolute;left:118px;top:96px;width:230px;text-align:center}
.f-brand i{display:block;width:48px;height:62px;margin:0 auto 12px;background:var(--gold);opacity:.85}
.f-brand h3{font-family:"Marcellus",serif;font-weight:400;font-size:22px;color:#f0e9df}
.socials{display:flex;justify-content:center;gap:10px;margin-top:14px}
.socials span{width:28px;height:28px;border-radius:50%;border:1px solid #7b6a4e}
.f-col{position:absolute;top:75px}
.f-col h5{font-family:"Gilda Display",serif;font-weight:400;font-size:12px;color:#d8d0c3}
.f-col ul{margin-top:34px;font-size:9px;line-height:18.8px;color:#fff}
.f-col li::before{content:"›";color:var(--gold);margin-right:6px}
.f-contact{font-size:7px;color:#9b948a;margin-top:34px;line-height:11px}
.f-contact b{display:block;font-weight:400;color:#fff;font-size:9px;line-height:12px;margin:2px 0 8px}
.news-in{margin-top:28px;width:200px;height:30px;border-bottom:1px solid #4b4239;font-size:8px;color:#7b746c;padding:10px 0 0 20px;position:relative}
.bottom{position:absolute;left:140px;right:140px;top:306px;display:flex;font-size:9px;color:#fff}
.bottom span:last-child{margin-left:auto;display:flex;gap:38px}
</style>
</head>
<body>

<header class="hero">
  <div role="img" aria-label="City skyline with tall towers above a tree-lined river at dusk" class="abs" style="inset:0;background:linear-gradient(180deg,rgba(20,18,16,.55) 0%,rgba(50,45,40,.15) 40%,rgba(90,55,25,.35) 80%,rgba(40,25,15,.6) 100%)"></div>
  <nav class="nav">
    <div class="brand"><span class="mark"></span>Verin Court Nine</div>
    <ul class="menu">
      <li class="active" style="left:0">HOME</li>
      <li style="left:52px">PROPERTIES</li>
      <li style="left:132px">SERVICES</li>
      <li style="left:200px">BLOGS</li>
      <li style="left:259px">ABOUT US</li>
      <li style="left:330px">CONTACT US</li>
      <li style="left:405px">EN ⌄</li>
    </ul>
    <div class="phone-btn"><svg width="10" height="10" viewBox="0 0 24 24" fill="none" stroke="#3a2a18" stroke-width="2"><path d="M5 3h4l2 5-3 2a12 12 0 0 0 6 6l2-3 5 2v4a2 2 0 0 1-2 2A18 18 0 0 1 3 5a2 2 0 0 1 2-2z"/></svg>+971 555 013 247</div>
    <svg class="search-ic" width="12" height="12" viewBox="0 0 24 24" fill="none" stroke="#fff" stroke-width="2"><circle cx="10" cy="10" r="7"/><path d="M15 15l6 6"/></svg>
  </nav>
  <div class="hero-copy">
    <div class="eyebrow">Welcome to Verin Court</div>
    <h1>Find Your Dream Property In<br>The Verin Court Nine</h1>
    <p>A Team Of Professionals Ready To Assist.</p>
  </div>
  <svg class="chev" width="16" height="18" viewBox="0 0 16 18" fill="none" stroke="#fff" stroke-width="1.5"><path d="M3 3l5 5 5-5M3 9l5 5 5-5"/></svg>
  <div class="quick-contact">
    <span style="background:#d9a94a"><svg width="11" height="11" viewBox="0 0 24 24" fill="none" stroke="#fff" stroke-width="2"><path d="M5 3h4l2 5-3 2a12 12 0 0 0 6 6l2-3 5 2v4a2 2 0 0 1-2 2A18 18 0 0 1 3 5a2 2 0 0 1 2-2z"/></svg></span>
    <span style="background:#f07a2a"><svg width="11" height="11" viewBox="0 0 24 24" fill="none" stroke="#fff" stroke-width="2"><rect x="3" y="5" width="18" height="14"/><path d="M3 6l9 7 9-7"/></svg></span>
    <span style="background:#2ebd4e"><svg width="11" height="11" viewBox="0 0 24 24" fill="none" stroke="#fff" stroke-width="2"><path d="M4 20l1.5-4A8 8 0 1 1 9 19z"/></svg></span>
    <span style="background:#1f8ef0"><svg width="11" height="11" viewBox="0 0 24 24" fill="none" stroke="#fff" stroke-width="2"><path d="M4 5h16v11H9l-5 4z"/></svg></span>
  </div>
  <form class="search">
    <div class="field"><b>⌂ Propert Type:</b>⌄</div>
    <div class="field"><b>⌂ Lodgly:</b>⌄</div>
    <div class="field"><b>▭ Bedroom:</b>⌄</div>
    <div class="field"><b>▦ Size:</b>⌄</div>
    <div class="field"><b>▢ Days:</b>⌄</div>
    <div class="search-btn"><svg width="9" height="9" viewBox="0 0 24 24" fill="none" stroke="#3a2a18" stroke-width="2.5"><circle cx="10" cy="10" r="7"/><path d="M15 15l6 6"/></svg>SEARCH</div>
  </form>
</header>

<section class="dev-band">
  <div class="reserve">
    <div class="brand-sm"><i></i>Verin Court Nine</div>
    <h2>Reserve Your Place in Your Future Home!</h2>
  </div>
  <div class="dev-title eyebrow">Properties by developers</div>
  <div class="dev-row">
    <span class="arrow" style="left:156px;top:20px">‹</span>
    <div class="logo" style="left:216px">Halvorn</div>
    <div class="logo" style="left:363px">Marlowe Tides</div>
    <div class="logo on" style="left:528px">Brevanta Homes</div>
    <div class="logo" style="left:692px">Calloway Group</div>
    <div class="logo" style="left:845px">Northvane</div>
    <span class="arrow" style="left:1044px;top:20px">›</span>
  </div>
</section>
<div class="emblem" style="left:570px;top:831px"><i></i></div>

<section>
  <div class="sec-head" style="top:926px">
    <div class="eyebrow">Top selling</div>
    <h2>Monthly &nbsp;<em>Highlights</em></h2>
  </div>
  <article class="card" style="left:159px;top:1024px">
    <div class="card-media" role="img" aria-label="Warm bedroom with upholstered headboard and lamps" style="background:linear-gradient(160deg,#7a5a3a,#c9a478 60%,#efe3d0)"></div>
    <span class="star"><svg width="8" height="8" viewBox="0 0 24 24" fill="#fff"><path d="M12 2l3 7 7 .5-5.5 4.5 2 7L12 17l-6.5 4 2-7L2 9.5 9 9z"/></svg></span><span class="gal"><svg width="9" height="9" viewBox="0 0 24 24" fill="none" stroke="#333" stroke-width="2"><rect x="3" y="6" width="18" height="13"/><circle cx="12" cy="12.5" r="3"/></svg></span>
    <h3>Lorem Ipsum</h3><p>Come home to a space where you and your family can grow-where you will live your happiest memories.</p>
    <ul class="specs"><li>▭ 4 Beds</li><li>◒ 2 Bath</li><li>⚇ 14 Guests</li></ul>
  </article>
  <article class="card" style="left:385px;top:1024px">
    <div class="card-media" role="img" aria-label="Bright bedroom with wooden floor and city view" style="background:linear-gradient(160deg,#d9d2c6,#a8927a 60%,#6a5440)"></div>
    <span class="star"><svg width="8" height="8" viewBox="0 0 24 24" fill="#fff"><path d="M12 2l3 7 7 .5-5.5 4.5 2 7L12 17l-6.5 4 2-7L2 9.5 9 9z"/></svg></span><span class="gal"><svg width="9" height="9" viewBox="0 0 24 24" fill="none" stroke="#333" stroke-width="2"><rect x="3" y="6" width="18" height="13"/><circle cx="12" cy="12.5" r="3"/></svg></span>
    <h3>Lorem Ipsum</h3><p>Come home to a space where you and your family can grow-where you will live your happiest memories.</p>
    <ul class="specs"><li>▭ 4 Beds</li><li>◒ 2 Bath</li><li>⚇ 14 Guests</li></ul>
  </article>
  <article class="card featured" style="left:611px;top:1024px">
    <div class="card-media" role="img" aria-label="Living room with grey sofa and tall windows" style="background:linear-gradient(160deg,#55575a,#b9b3aa 55%,#e6e1d8)"></div>
    <span class="star"><svg width="8" height="8" viewBox="0 0 24 24" fill="#fff"><path d="M12 2l3 7 7 .5-5.5 4.5 2 7L12 17l-6.5 4 2-7L2 9.5 9 9z"/></svg></span><span class="gal"><svg width="11" height="11" viewBox="0 0 24 24" fill="none" stroke="#fff" stroke-width="2"><rect x="3" y="6" width="18" height="13"/><circle cx="12" cy="12.5" r="3"/></svg></span>
    <h3>Lorem Ipsum</h3><p>Come home to a space where you and your family can grow-where you will live your happiest memories.</p>
    <ul class="specs"><li>▭ 4 Beds</li><li>◒ 2 Bath</li><li>⚇ 14 Guests</li></ul>
  </article>
  <article class="card" style="left:838px;top:1024px">
    <div class="card-media" role="img" aria-label="Lounge with plants and floor lamp" style="background:linear-gradient(160deg,#8a8f6a,#cfc6b4 60%,#9c8c76)"></div>
    <span class="star"><svg width="8" height="8" viewBox="0 0 24 24" fill="#fff"><path d="M12 2l3 7 7 .5-5.5 4.5 2 7L12 17l-6.5 4 2-7L2 9.5 9 9z"/></svg></span><span class="gal"><svg width="9" height="9" viewBox="0 0 24 24" fill="none" stroke="#333" stroke-width="2"><rect x="3" y="6" width="18" height="13"/><circle cx="12" cy="12.5" r="3"/></svg></span>
    <h3>Lorem Ipsum</h3><p>Come home to a space where you and your family can grow-where you will live your happiest memories.</p>
    <ul class="specs"><li>▭ 4 Beds</li><li>◒ 2 Bath</li><li>⚇ 14 Guests</li></ul>
  </article>
</section>

<section class="launch">
  <div class="sec-head" style="top:60px">
    <div class="eyebrow">Properties</div>
    <h2>Latest &nbsp;<em>Launch</em></h2>
  </div>
  <div class="tile" style="left:109px;top:149px;width:398px;height:188px" role="img" aria-label="Luxury bedroom with panelled walls"><div style="height:100%;background:linear-gradient(120deg,#4a3a2c,#a48c72 55%,#d9cbb6)"></div><span class="tag">Lorem Ipsum</span></div>
  <div class="tile" style="left:527px;top:149px;width:314px;height:188px" role="img" aria-label="Dim lounge with wood tones"><div style="height:100%;background:linear-gradient(160deg,#6a4a2c,#3a281a 60%,#1e1610)"></div>
    <div class="overlay"><h4>Lorem Ipsum</h4><p>Lorem Ipsum is simply dummy text of the printing and typesetting industry. Lorem Ipsum has been the industry's standard dummy.</p></div><span class="go">›</span></div>
  <div class="tile" style="left:859px;top:149px;width:231px;height:188px" role="img" aria-label="White living room with staircase"><div style="height:100%;background:linear-gradient(140deg,#efe8dc,#c9b89a 60%,#8c7456)"></div><span class="tag">Lorem Ipsum</span></div>
  <div class="tile" style="left:109px;top:357px;width:231px;height:190px" role="img" aria-label="Grey bedroom with large window"><div style="height:100%;background:linear-gradient(140deg,#5d6064,#b8b6b0 55%,#e5e2dc)"></div><span class="tag">Lorem Ipsum</span></div>
  <div class="tile" style="left:359px;top:357px;width:397px;height:190px" role="img" aria-label="Modern lounge with sofa and TV wall"><div style="height:100%;background:linear-gradient(120deg,#8c8276,#cfc7bb 50%,#5a544c)"></div><span class="tag">Lorem Ipsum</span></div>
  <div class="tile" style="left:776px;top:357px;width:314px;height:190px" role="img" aria-label="Living room with stone accent wall"><div style="height:100%;background:linear-gradient(120deg,#3e342a,#8a7560 50%,#d4cbc0)"></div><span class="tag">Lorem Ipsum</span></div>
</section>

<div class="partners-title">OUR PARTNERS</div>
<span class="arrow" style="left:108px;top:2122px;color:#999">‹</span>
<div class="partner" style="left:158px">Quill Group</div>
<div class="partner" style="left:308px;font-weight:600">Ravelo</div>
<div class="partner on" style="left:459px"><span role="img" aria-label="Tessamor partner badge"></span></div>
<div class="partner" style="left:608px">Lumora</div>
<div class="partner" style="left:759px">Averton Estates</div>
<div class="partner" style="left:910px">Pelham</div>
<span class="arrow" style="left:1080px;top:2122px;color:#999">›</span>

<section class="feat">
  <div role="img" aria-label="Dark luxury interior backdrop" class="abs" style="inset:0;background:radial-gradient(ellipse at 30% 20%,rgba(120,80,40,.35),transparent 60%)"></div>
  <div class="sec-head" style="top:60px">
    <div class="eyebrow">Luxury</div>
    <h2>Featured &nbsp;<em>Properties</em></h2>
  </div>
  <article class="card" style="left:159px;top:160px">
    <div class="card-media" role="img" aria-label="Living room with night city view" style="background:linear-gradient(160deg,#1f2f55,#5a5a6a 50%,#a08a6a)"></div>
    <span class="star"><svg width="8" height="8" viewBox="0 0 24 24" fill="#fff"><path d="M12 2l3 7 7 .5-5.5 4.5 2 7L12 17l-6.5 4 2-7L2 9.5 9 9z"/></svg></span><span class="gal"><svg width="9" height="9" viewBox="0 0 24 24" fill="none" stroke="#333" stroke-width="2"><rect x="3" y="6" width="18" height="13"/><circle cx="12" cy="12.5" r="3"/></svg></span>
    <h3>Lorem Ipsum</h3><p>Come home to a space where you and your family can grow-where you will live your happiest memories.</p>
    <ul class="specs"><li>▭ 4 Beds</li><li>◒ 2 Bath</li><li>⚇ 14 Guests</li></ul>
  </article>
  <article class="card featured" style="left:385px;top:160px">
    <div class="card-media" role="img" aria-label="Dark lounge with blue chairs and plants" style="background:linear-gradient(160deg,#2c2e30,#56585a 50%,#1f3a55)"></div>
    <span class="star"><svg width="8" height="8" viewBox="0 0 24 24" fill="#fff"><path d="M12 2l3 7 7 .5-5.5 4.5 2 7L12 17l-6.5 4 2-7L2 9.5 9 9z"/></svg></span><span class="gal" style="background:#fff;width:22px;height:22px;top:164px"><svg width="9" height="9" viewBox="0 0 24 24" fill="none" stroke="#333" stroke-width="2"><rect x="3" y="6" width="18" height="13"/><circle cx="12" cy="12.5" r="3"/></svg></span>
    <h3>Lorem Ipsum</h3><p>Come home to a space where you and your family can grow-where you will live your happiest memories.</p>
    <ul class="specs"><li>▭ 4 Beds</li><li>◒ 2 Bath</li><li>⚇ 14 Guests</li></ul>
  </article>
  <article class="card" style="left:611px;top:160px">
    <div class="card-media" role="img" aria-label="Bedroom with mustard cushions" style="background:linear-gradient(160deg,#d6d2cc,#b4a894 55%,#d09a3a)"></div>
    <span class="star"><svg width="8" height="8" viewBox="0 0 24 24" fill="#fff"><path d="M12 2l3 7 7 .5-5.5 4.5 2 7L12 17l-6.5 4 2-7L2 9.5 9 9z"/></svg></span><span class="gal" style="background:var(--gold-light);width:30px;height:30px;top:158px"><svg width="11" height="11" viewBox="0 0 24 24" fill="none" stroke="#fff" stroke-width="2"><rect x="3" y="6" width="18" height="13"/><circle cx="12" cy="12.5" r="3"/></svg></span>
    <h3>Lorem Ipsum</h3><p>Come home to a space where you and your family can grow-where you will live your happiest memories.</p>
    <ul class="specs"><li>▭ 4 Beds</li><li>◒ 2 Bath</li><li>⚇ 14 Guests</li></ul>
  </article>
  <article class="card" style="left:838px;top:160px">
    <div class="card-media" role="img" aria-label="White living room with shelving" style="background:linear-gradient(160deg,#eef0f2,#b9bcc0 55%,#6c7076)"></div>
    <span class="star"><svg width="8" height="8" viewBox="0 0 24 24" fill="#fff"><path d="M12 2l3 7 7 .5-5.5 4.5 2 7L12 17l-6.5 4 2-7L2 9.5 9 9z"/></svg></span><span class="gal"><svg width="9" height="9" viewBox="0 0 24 24" fill="none" stroke="#333" stroke-width="2"><rect x="3" y="6" width="18" height="13"/><circle cx="12" cy="12.5" r="3"/></svg></span>
    <h3>Lorem Ipsum</h3><p>Come home to a space where you and your family can grow-where you will live your happiest memories.</p>
    <ul class="specs"><li>▭ 4 Beds</li><li>◒ 2 Bath</li><li>⚇ 14 Guests</li></ul>
  </article>
</section>
<div class="emblem" style="left:570px;top:2747px"><i></i></div>

<section>
  <div class="sec-head" style="top:2836px">
    <div class="eyebrow">Blogs</div>
    <h2>Latest &nbsp;<em>Articles</em></h2>
  </div>
  <article class="post dark" style="left:119px;top:2937px;width:472px">
    <div class="ph" role="img" aria-label="Group of friends chatting in a dining room" style="background:linear-gradient(140deg,#e6dccd,#b79a78 60%,#7a5a3a)"></div>
    <div class="txt"><div class="date" style="color:#fff">MAY 3, 2024</div><h4>Lorem Ipsum is simply dummy text of the.</h4><p>Lorem Ipsum is simply dummy text of the printing and typesetting industry.</p><div class="more">READ ARTICLE</div></div>
  </article>
  <article class="post" style="left:608px;top:2937px;width:473px">
    <div class="ph" role="img" aria-label="Couple cooking in a bright kitchen" style="background:linear-gradient(140deg,#d8d4cc,#9a948a 55%,#5a5450)"></div>
    <div class="txt"><div class="date">MAY 3, 2024</div><h4>Lorem Ipsum is simply dummy text of the.</h4><p>Lorem Ipsum is simply dummy text of the printing and typesetting industry.</p><div class="more">READ ARTICLE</div></div>
  </article>
  <article class="post" style="left:119px;top:3146px;width:472px">
    <div class="txt"><div class="date">MAY 3, 2024</div><h4>Lorem Ipsum is simply dummy text of the.</h4><p>Lorem Ipsum is simply dummy text of the printing and typesetting industry.</p><div class="more">READ ARTICLE</div></div>
    <div class="ph" role="img" aria-label="Agent showing a client an apartment" style="background:linear-gradient(140deg,#8a8c8e,#c4bcae 55%,#6a5a48)"></div>
  </article>
  <article class="post" style="left:608px;top:3146px;width:473px">
    <div class="txt"><div class="date">MAY 3, 2024</div><h4>Lorem Ipsum is simply dummy text of the.</h4><p>Lorem Ipsum is simply dummy text of the printing and typesetting industry.</p><div class="more">READ ARTICLE</div></div>
    <div class="ph" role="img" aria-label="Couple viewing a bright apartment" style="background:linear-gradient(140deg,#e8e4dc,#b8aa98 55%,#7a5e46)"></div>
  </article>
</section>

<div class="strip-title">PROPERTIES</div>
<div class="strip">
  <div role="img" aria-label="Visitors touring a property" style="background:linear-gradient(160deg,#6a6662,#a89a88)"></div>
  <div role="img" aria-label="Warm living room" style="background:linear-gradient(160deg,#5a4430,#c8a878)"></div>
  <div role="img" aria-label="Modern building facade" style="background:linear-gradient(160deg,#2a4a7a,#c8ccd2)"></div>
  <div role="img" aria-label="Couple in a kitchen" style="background:linear-gradient(160deg,#a89c8c,#4a4038)"></div>
  <div role="img" aria-label="Apartment block exterior" style="background:linear-gradient(160deg,#3a3e44,#8c929a)"></div>
  <div role="img" aria-label="Lounge with teal accents" style="background:linear-gradient(160deg,#c8bca8,#3a6a6a)"></div>
  <div role="img" aria-label="Bright living area with chandelier" style="background:linear-gradient(160deg,#eae6de,#a89a86)"></div>
  <div role="img" aria-label="Bedroom with warm lighting" style="background:linear-gradient(160deg,#8a6a48,#d8c4a4)"></div>
</div>

<footer class="footer">
  <div class="f-brand"><i></i><h3>Verin Court Nine</h3>
    <div class="socials"><span aria-label="Professional network"></span><span aria-label="Photo network"></span><span aria-label="Microblog"></span><span aria-label="Social network"></span></div>
  </div>
  <div class="f-col" style="left:404px"><h5>Quick Links</h5><ul><li>Home</li><li>Properties</li><li>Services</li><li>Blogs</li><li>About Us</li><li>Contact Us</li></ul></div>
  <div class="f-col" style="left:528px"><h5>Help</h5><ul><li>Help center</li><li>FAQs</li><li>Privacy policy</li><li>Cookie policy</li><li>Terms of use</li><li>Cookie settings</li></ul></div>
  <div class="f-col" style="left:666px;width:170px"><h5>Contact Us</h5>
    <div class="f-contact">ADDRESS :<b>It is a long established fact that a reader will be distracted</b>PHONE :<b>+971 555 013 247</b>MAIL US :<b>desk@verincourtnine.com</b></div>
  </div>
  <div class="f-col" style="left:853px"><h5>Newsletter</h5>
    <div class="f-contact" style="margin-top:34px">Subscribe our mailing list.</div>
    <div class="news-in">Email...<svg style="position:absolute;right:4px;top:10px" width="12" height="12" viewBox="0 0 24 24" fill="none" stroke="#c9a24a" stroke-width="2"><path d="M3 12l18-8-7 18-3-7z"/></svg></div>
  </div>
  <div class="bottom"><span>Verin Court Nine © 2005–2024</span><span><span>Privacy policy</span><span>Cookie policy</span></span></div>
</footer>

</body>
</html>
```